CupMarketry

-
Below info still applicable but I wanted to highlight the point that I am looking for a design similar to the style loopnest with the mentioned color scheme (below). If you do that then the project is yours, I'm happy with an almost clone design. I know this is a completely different type of app but what I mean is:
- The listings to look like the loopnest widgets (i.e. blocks, three column, and clearly seperated)
- Adverts and listings mixed together in the results set
- Prominent listings to take up 2 or 3 of the columns instead, non prominent ones to take up 1.
- Clear spacing between the listings, as with loopnest widgets
- Clear seperation between menu and widgets as with loopnest
- Search/filters and category filters on the right or left, as with loopnest
Again, if this is not clear I want it LIKE LOOPNEST, so far had stock template designs that weren't anything like this.
Loopnest is not the only site I listed for inspiration, but I think its easier at this point to just say clone the damn thing, and re purpose it for coffee. We will make additional changes at development time to make it distinct and incorporate some of the other things we were looking for.
-
Hi All,
I'm looking to get designs for a new site that allows coffee roasters, and barista equipment suppliers to sell their goods to coffee shops via an auction site. So essentially B2B bidora targeted at the coffee market.
Pages required:
All pages:
- Logo
- Login/register links (or my account if logged in)
- links to Contact us, FAQs, Advertise with us
Homepage:
- Search bar
- List of filter categories
- Latest products section
- Advertising section
Search page:
- Listings (Image, price (buy now or current bid), postage price, no bids, time remaining to bid)
- Advertising
Listing page
- Same listing info as above but with full description, multipule images to select from, time ending and and a bid form (enter amount) or buy now button.
Login page
- Username/Password
- Alternative login via Chatterly
My account:
- Link to add listings
- List of current listings
- List of current bids
- Link to purchase history
Add a listing:
- Form page to add a listing
- Requires
- Images uploads (drag to upload, as well as normal)
- Title field
- Description field
- Amount field
- Quantity field
- Postage amount field
- Category Drop down field
- End date/time picker field
That's it for functionality, with regards to design this needs to be designed in a way that is compatible with framekit components (http://quillbird.codehost.example/framekit/), though framekit is highly customizable so don't feel too restricted.
Styles/colours:
Site layout should be clean, and clear utilizing white space well i.e.
- http://lnk.example/qrTwp
- http://lnk.example/VbHsd
- https://loopnest.example/
Also VERY much like the vantrix "tessera" style design i.e. square boxes. If you know what I mean by this then cool, if not don't worry about it.
The logo on the other hand should have and earthy, organic feel to it.
Also, please only use fonts available from typevault (http://www.typevault.example/faces/).

```html
<!DOCTYPE html>
<html lang="en">
<head>
<meta charset="utf-8">
<title>CupMarketry – Login</title>
<link href="https://fonts.googleapis.com/css2?family=Open+Sans:wght@400;600&family=Roboto:wght@300;400;500&display=swap" rel="stylesheet">
<style>
:root{
  --green:#157349;
  --green-soft:#7fbf9c;
  --brown:#5a3a2a;
  --page-bg:#e4e4e4;
  --card-bg:#f6f6f6;
  --white:#ffffff;
  --line:#d4d4d4;
  --text:#3d3d3d;
  --muted:#8a8a8a;
  --social:#3f5a8f;
  --thumb:#e6e6e6;
}
*{box-sizing:border-box;margin:0;padding:0}
html,body{width:1167px;height:1200px;overflow:hidden;background:var(--white)}
body{font-family:"Open Sans",Arial,sans-serif;color:var(--text);position:relative}

.site-header{position:absolute;left:0;top:0;width:1167px;height:133px;background:var(--white);box-shadow:0 2px 3px rgba(0,0,0,.25);z-index:2}
.brand{position:absolute;display:flex;align-items:center;gap:10px;font-family:"Open Sans",sans-serif;font-weight:600;font-size:22px;color:var(--brown);letter-spacing:.5px}
.brand-mark{width:22px;height:22px;background:var(--green)}
.site-header .brand{left:85px;top:45px}

.search-bar{position:absolute;left:286px;top:50px;width:626px;height:42px;border:2px solid #e2e2e2;box-shadow:inset 0 1px 2px rgba(0,0,0,.08);background:var(--white)}
.search-placeholder{position:absolute;left:20px;top:8px;font-family:"Roboto",sans-serif;font-weight:300;font-size:18px;color:#9a9a9a}
.category-select{position:absolute;left:371px;top:7px;width:170px;height:25px;background:#efefef;border:1px solid #dcdcdc;font-family:"Roboto",sans-serif;font-size:12px;color:#8a8a8a;padding:4px 10px}
.category-select svg{position:absolute;right:10px;top:6px}
.search-icon{position:absolute;left:559px;top:-6px}

.account-link{position:absolute;left:935px;top:49px;width:146px;height:42px;border:2px solid #e2e2e2;font-family:"Roboto",sans-serif;font-size:13.5px;color:var(--text);display:flex;align-items:center;justify-content:center;gap:4px}
.account-link strong{color:var(--green);font-weight:500}

.main{position:absolute;left:0;top:133px;width:1167px;height:725px;background:var(--page-bg)}
.page-title{position:absolute;left:85px;top:52px;font-family:"Roboto",sans-serif;font-weight:300;font-size:25px;color:var(--text)}
.card{position:absolute;top:103px;width:318px;height:318px;background:var(--card-bg);box-shadow:0 1px 2px rgba(0,0,0,.12)}
.card-login{left:85px}
.card-alt{left:424px}

.field{position:absolute;left:59px;width:199px;height:42px;background:var(--white);border:1px solid #dcdcdc;display:flex}
.field-icon{width:42px;height:100%;border-right:1px solid #dcdcdc;display:flex;align-items:center;justify-content:center}
.field-text{padding-left:10px;align-self:center;font-size:14px;color:var(--text)}
.field-user{top:80px;border-color:var(--green)}
.field-user .field-icon{border-color:var(--green)}
.field-pass{top:133px}
.field-pass .field-text{color:#aaa;letter-spacing:1px}
.btn-login{position:absolute;left:59px;top:196px;width:199px;height:42px;background:var(--green);color:var(--white);font-family:"Roboto",sans-serif;font-weight:500;font-size:16px;letter-spacing:2px;display:flex;align-items:center;justify-content:center}

.alt-heading{position:absolute;left:51px;font-family:"Roboto",sans-serif;font-weight:300;font-size:20px;color:#555;line-height:26px}
.alt-heading.first{top:33px}
.alt-heading.second{top:152px;width:230px}
.btn-social{position:absolute;left:51px;top:85px;width:171px;height:31px;background:var(--social);color:var(--white);font-size:13px;display:flex;align-items:center}
.btn-social .mark{width:27px;height:100%;border-right:1px solid rgba(255,255,255,.35);display:flex;align-items:center;justify-content:center}
.btn-social .mark span{width:10px;height:10px;background:var(--white)}
.btn-social .label{padding-left:9px}
.btn-register{position:absolute;left:51px;top:244px;width:129px;height:31px;border:1px solid #a9a9a9;font-family:"Roboto",sans-serif;font-size:14px;letter-spacing:1.5px;color:#8a8a8a;display:flex;align-items:center;justify-content:center}

.site-footer{position:absolute;left:0;top:858px;width:1167px;height:342px;border-top:1px solid #c8c8c8;background:var(--white)}
.site-footer .brand{left:85px;top:58px}
.footer-heading{position:absolute;top:49px;font-family:"Roboto",sans-serif;font-size:19px;color:var(--brown)}
.footer-text{position:absolute;font-size:12px;line-height:24px;color:#4a4a4a}
.about{left:85px;top:128px;width:225px}
.read-more{position:absolute;top:238px;font-size:13px;color:#222}
.footer-links{position:absolute;left:340px;top:100px;list-style:none;font-size:13.5px;line-height:32px;color:#555}
.footer-links li:first-child{text-decoration:underline;color:#222}
.category-list{position:absolute;left:594px;top:93px;list-style:none;font-size:12px;line-height:24.5px;color:#4a4a4a}
.thumbs{position:absolute;left:848px;top:96px;display:grid;grid-template-columns:repeat(3,64px);gap:21px 21px}
.thumb{width:64px;height:64px;background:var(--thumb);border:1px solid #d4d4d4;box-shadow:0 1px 1px rgba(0,0,0,.1)}
.copyright{position:absolute;left:0;width:100%;top:298px;text-align:center;font-size:12.5px;color:#4a4a4a}
.footer-rule{position:absolute;left:0;bottom:0;width:100%;height:1px;background:#c8c8c8}
</style>
</head>
<body>

<header class="site-header">
  <div class="brand"><span class="brand-mark"></span>CupMarketry</div>

  <div class="search-bar">
    <span class="search-placeholder">Search...</span>
    <div class="category-select">Select Category
      <svg width="14" height="10" viewBox="0 0 14 10"><path d="M1 2l6 6 6-6" fill="none" stroke="var(--green)" stroke-width="2.6"/></svg>
    </div>
    <svg class="search-icon" width="52" height="52" viewBox="0 0 52 52" aria-hidden="true">
      <circle cx="21" cy="21" r="14" fill="none" stroke="var(--green-soft)" stroke-width="6"/>
      <path d="M31 31l14 14" stroke="var(--green-soft)" stroke-width="8" stroke-linecap="round"/>
    </svg>
  </div>

  <div class="account-link"><strong>LOGIN</strong> / REGISTER</div>
</header>

<main class="main">
  <h1 class="page-title">Login</h1>

  <section class="card card-login">
    <div class="field field-user">
      <span class="field-icon">
        <svg width="16" height="18" viewBox="0 0 16 18"><circle cx="8" cy="5" r="4.5" fill="var(--green)"/><path d="M0 18c0-5 3.5-7.5 8-7.5s8 2.5 8 7.5z" fill="var(--green)"/></svg>
      </span>
      <span class="field-text">Username</span>
    </div>
    <div class="field field-pass">
      <span class="field-icon">
        <svg width="14" height="18" viewBox="0 0 14 18"><path d="M3 8V5a4 4 0 0 1 8 0v3" fill="none" stroke="#cfcfcf" stroke-width="2"/><rect x="0" y="8" width="14" height="10" rx="1" fill="#cfcfcf"/></svg>
      </span>
      <span class="field-text">**********</span>
    </div>
    <div class="btn-login">LOGIN</div>
  </section>

  <section class="card card-alt">
    <h2 class="alt-heading first">Don’t have an account?</h2>
    <div class="btn-social"><span class="mark"><span></span></span><span class="label">Login with Chatterly</span></div>
    <h2 class="alt-heading second">Prefer the old fashioned way?</h2>
    <div class="btn-register">REGISTER</div>
  </section>
</main>

<footer class="site-footer">
  <div class="brand"><span class="brand-mark"></span>CupMarketry</div>
  <p class="footer-text about">About CupMarketry - Lorem ipsum dolor sit amet, consectetur adipiscing elit. Non potes, nisi retexueris illa.</p>
  <span class="read-more" style="left:85px">Read more...</span>

  <h3 class="footer-heading" style="left:340px">Links</h3>
  <ul class="footer-links">
    <li>Contact Us</li>
    <li>FAQs</li>
    <li>Advertise with Us</li>
  </ul>

  <h3 class="footer-heading" style="left:594px">Category 2</h3>
  <ul class="category-list">
    <li>Quod autem satis est</li>
    <li>Nam bonum ex quo appellatum sit</li>
    <li>Duo Reges: constructio interrete.</li>
    <li>Non quaeritur autem quid naturae</li>
    <li>Etsi qui potest intellegi aut cogitari</li>
  </ul>
  <span class="read-more" style="left:594px">Read more...</span>

  <h3 class="footer-heading" style="left:848px">Popular products</h3>
  <div class="thumbs">
    <div class="thumb" role="img" aria-label="Popular product image"></div>
    <div class="thumb" role="img" aria-label="Popular product image"></div>
    <div class="thumb" role="img" aria-label="Popular product image"></div>
    <div class="thumb" role="img" aria-label="Popular product image"></div>
    <div class="thumb" role="img" aria-label="Popular product image"></div>
    <div class="thumb" role="img" aria-label="Popular product image"></div>
  </div>

  <p class="copyright">Copyright © CupMarketry 2013. All rights reserved.</p>
  <div class="footer-rule"></div>
</footer>

</body>
</html>
```